Flyer-Design für Vermietung von Zelten, Wasserparks und Hüpfburgen
Zielgruppe
Vermietung Inflatables Zelte - Wasserparks- Hüpfburgen Zielgruppe: Firmen und Vereine Public Viewing.
Es soll nicht wie unser A4 Folder sein. Das ist KEINE Vorgabe. Die Designer sollen kreativ sein und das Endergebnis ist ein A4-Blatt dass 2x gefaltet in ein Standardkuvert muss.
Aufgabenstellung
Peppig - Modern - Sportlich
Public Viewing TK2031 Muster ist hinzugefügt was drauf sein sollte

```html
<!DOCTYPE html>
<html lang="de">
<head>
<meta charset="utf-8">
<title>Sommer 2031 – Public Viewing Flyer</title>
<link href="https://fonts.googleapis.com/css2?family=Montserrat:wght@400;600;800&family=Raleway:wght@400;600;700&display=swap" rel="stylesheet">
<style>
  :root{
    --paper:#ecebe8;
    --grey:#5b5e61;
    --grey-dark:#46494c;
    --yellow:#f7d21a;
    --yellow-soft:#fbd85a;
    --orange:#f0962a;
    --white:#ffffff;
  }
  *{box-sizing:border-box;margin:0;padding:0}
  html,body{width:1200px;height:1200px;overflow:hidden;background:var(--paper)}
  body{position:relative;font-family:"Raleway",sans-serif;color:var(--white)}
  .sheet{position:absolute;left:40px;width:1120px;height:540px;overflow:hidden;box-shadow:0 6px 18px rgba(0,0,0,.15)}
  .sheet--outside{top:40px}
  .sheet--inside{top:620px}
  .sheet svg.shapes{position:absolute;inset:0;width:100%;height:100%}
  .abs{position:absolute}

  /* outside: price panel */
  .price-title{left:28px;top:26px;font-size:20px;font-weight:600}
  .price-table{left:28px;top:66px;width:330px;border-collapse:collapse;font-size:11px}
  .price-table th{font-weight:400;font-size:8px;color:var(--white);padding:2px 4px;text-align:center}
  .price-table td{background:rgba(255,255,255,.9);color:#555;padding:5px 6px;border:1px solid var(--yellow);text-align:center}
  .price-table td.item{text-align:left;width:110px}
  .price-table tr.note td{background:none;border:none;color:var(--white);text-align:left;font-size:9px;font-weight:700;padding:2px 2px 10px}
  .contact{left:392px;top:70px;font-size:10px;line-height:1.9}
  .contact h3{font-size:10px;font-weight:700;letter-spacing:.05em}
  .badge{left:400px;top:10px;width:70px;height:56px}
  .footnote{left:28px;top:470px;width:500px;font-size:7px;line-height:1.5}

  /* outside: cover */
  .brand{right:28px;top:22px;display:flex;align-items:center;gap:6px;font-family:"Montserrat",sans-serif;font-weight:600;font-size:18px;white-space:nowrap}
  .brand::before{content:"";width:14px;height:14px;border-radius:50%;background:var(--white)}
  .season{left:640px;top:70px;font-family:"Montserrat",sans-serif;font-weight:800;line-height:.9}
  .season span{display:block}
  .season .s1{font-size:40px}
  .season .s2{font-size:86px;border-bottom:6px solid var(--white);padding-bottom:4px;width:max-content}
  .pv{left:860px;top:288px;font-family:"Montserrat",sans-serif;font-weight:800;font-size:20px;line-height:1.05;text-align:center;width:120px}
  .special{left:820px;top:420px;font-family:"Montserrat",sans-serif;font-weight:800;font-size:20px;line-height:1.15}
  .cities{left:700px;top:505px;font-size:11px;letter-spacing:.03em;white-space:nowrap}

  /* inside */
  .headline{left:372px;top:440px;font-family:"Montserrat",sans-serif;font-weight:800;font-size:40px;line-height:1.1;transform:rotate(-30deg);transform-origin:left top;white-space:nowrap}
  .services{left:745px;top:330px;font-family:"Montserrat",sans-serif;font-weight:800;font-size:17px;line-height:1.35;transform:rotate(-15deg);transform-origin:left top;white-space:nowrap}
  .services .cta{color:var(--yellow);font-size:17px;margin-top:10px;display:block}
</style>
</head>
<body>

<section class="sheet sheet--outside">
  <svg class="shapes" viewBox="0 0 1120 540" xmlns="http://www.w3.org/2000/svg">
    <defs>
      <linearGradient id="bounceTone" x1="0" y1="0" x2="1" y2="1">
        <stop offset="0" stop-color="#f4a23a"/>
        <stop offset=".5" stop-color="#f9cf3e"/>
        <stop offset="1" stop-color="#f6b63a"/>
      </linearGradient>
      <linearGradient id="coverPhoto" x1="0" y1="0" x2="1" y2="1">
        <stop offset="0" stop-color="#e79a3f"/>
        <stop offset=".6" stop-color="#c9b98a"/>
        <stop offset="1" stop-color="#9aa7a0"/>
      </linearGradient>
    </defs>
    <rect x="0" y="0" width="560" height="540" fill="url(#bounceTone)" role="img" aria-label="Foto: Kinder auf einer gelb-orangen Hüpfburg"/>
    <polygon points="0,440 560,380 560,540 0,540" fill="var(--grey)"/>
    <polygon points="0,440 120,427 0,390" fill="var(--yellow)"/>

    <rect x="560" y="0" width="560" height="260" fill="url(#coverPhoto)" role="img" aria-label="Foto: Public-Viewing-Zelt mit Besuchern"/>
    <polygon points="560,150 1120,260 1120,540 560,540" fill="var(--grey)"/>
    <polygon points="560,150 760,190 560,330" fill="var(--grey-dark)"/>
    <polygon points="820,270 1020,270 920,400" fill="var(--yellow)"/>
    <polygon points="560,440 680,470 560,540" fill="var(--yellow)"/>
    <polygon points="1120,180 1120,330 1030,250" fill="var(--grey-dark)"/>
  </svg>

  <h2 class="abs price-title">Preisübersicht</h2>
  <table class="abs price-table">
    <tr><th></th><th>1 Tag</th><th>Wochenende</th><th>Woche</th></tr>
    <tr><td class="item">Fußball TK*</td><td>1.100,-</td><td>1.800,-</td><td>Anfrage</td></tr>
    <tr class="note"><td colspan="4">Bild- und Tontechnik, Überdachung je nach Besucherzahl</td></tr>
    <tr><td class="item">Kino mit Filmen</td><td>1.000,-</td><td>1.000,-</td><td>1.000,-</td></tr>
    <tr class="note"><td colspan="4">Beliebige Filme der Studios Nordlicht Pictures, Kaskade Film, Fabelhaus, Orbis und LINDWURM FILMS</td></tr>
    <tr><td class="item">Fun 4 Kids</td><td>1.000,-</td><td>1.000,-</td><td>1.000,-</td></tr>
    <tr class="note"><td colspan="4">Zwei Attraktionen nach Wahl für die Unterhaltung der jüngsten Besucher</td></tr>
    <tr><td class="item">Kombi – ALLE 3 Pakete</td><td>2.900,-</td><td>3.600,-</td><td>Anfrage</td></tr>
  </table>

  <svg class="abs badge" viewBox="0 0 70 56" xmlns="http://www.w3.org/2000/svg">
    <polygon points="35,0 42,8 53,4 54,15 66,17 60,27 68,36 57,40 57,52 46,48 38,56 32,48 21,53 19,42 8,40 13,30 3,22 14,17 13,6 25,8" fill="var(--grey)"/>
    <text x="35" y="25" font-family="Raleway, sans-serif" font-size="7" fill="#fff" text-anchor="middle">SONDER</text>
    <text x="35" y="35" font-family="Raleway, sans-serif" font-size="7" fill="#fff" text-anchor="middle">AKTION!</text>
  </svg>

  <div class="abs contact">
    <h3>KONTAKT</h3>
    <p>+43 (0)660 4128300</p>
    <p>+49 (0)151 2208374</p>
    <p>+49 (0)8341 557210</p>
    <p>office@blaswerk-events.at</p>
    <p>www.blaswerk-events.at</p>
  </div>

  <p class="abs footnote">Alle Preise in EUR pro Wochenende zzgl. gesetzlicher MwSt. Transport, Auf- und Abbau nach Vereinbarung. Gastronomie und Personal auf Anfrage.</p>

  <div class="abs brand">Blaswerk</div>
  <h1 class="abs season"><span class="s1">Sommer</span><span class="s2">2031</span></h1>
  <p class="abs pv">public viewing</p>
  <p class="abs special">mit unserem TK 2031<br>SPECIAL</p>
  <p class="abs cities">Bregenz &nbsp;|&nbsp; Lindau &nbsp;|&nbsp; Au (St. Gallen) &nbsp;|&nbsp; Wien &nbsp;|&nbsp; Graz</p>
</section>

<section class="sheet sheet--inside">
  <svg class="shapes" viewBox="0 0 1120 540" xmlns="http://www.w3.org/2000/svg">
    <defs>
      <linearGradient id="insideTone" x1="0" y1="0" x2="1" y2="1">
        <stop offset="0" stop-color="#fbd04a"/>
        <stop offset=".5" stop-color="#f6a83a"/>
        <stop offset="1" stop-color="#fbd85a"/>
      </linearGradient>
      <linearGradient id="tentTone" x1="0" y1="0" x2="0" y2="1">
        <stop offset="0" stop-color="#e9e6ef"/>
        <stop offset="1" stop-color="#8d8a9c"/>
      </linearGradient>
      <linearGradient id="outdoorTone" x1="0" y1="0" x2="0" y2="1">
        <stop offset="0" stop-color="#cfd9e4"/>
        <stop offset="1" stop-color="#6f8a5a"/>
      </linearGradient>
      <linearGradient id="dartTone" x1="0" y1="0" x2="1" y2="1">
        <stop offset="0" stop-color="#4d5054"/>
        <stop offset="1" stop-color="#2f3134"/>
      </linearGradient>
    </defs>
    <rect width="1120" height="540" fill="url(#insideTone)" role="img" aria-label="Foto: aufblasbares Element in Gelb und Orange"/>

    <g role="img" aria-label="Fotoraster: aufblasbare Eventzelte innen und außen, Konferenzbestuhlung, Wasserpark">
      <rect x="15" y="15" width="120" height="160" fill="url(#outdoorTone)"/>
      <rect x="145" y="15" width="120" height="160" fill="url(#tentTone)"/>
      <rect x="275" y="15" width="90" height="160" fill="url(#outdoorTone)"/>
      <rect x="15" y="185" width="120" height="160" fill="url(#tentTone)"/>
      <rect x="145" y="185" width="120" height="160" fill="url(#tentTone)"/>
      <rect x="275" y="185" width="90" height="160" fill="url(#outdoorTone)"/>
      <rect x="15" y="355" width="120" height="170" fill="url(#outdoorTone)"/>
      <rect x="145" y="355" width="120" height="170" fill="url(#tentTone)"/>
    </g>

    <rect x="830" y="0" width="290" height="220" fill="url(#tentTone)" role="img" aria-label="Foto: Zeltinnenraum mit Stehtischen"/>
    <polygon points="830,0 1120,0 1120,40 830,110" fill="var(--yellow-soft)" opacity=".7"/>

    <polygon points="730,260 1120,180 1120,540 700,540" fill="url(#dartTone)" role="img" aria-label="Foto: aufblasbare Fußball-Dartscheibe"/>
    <polygon points="730,260 940,217 820,330" fill="var(--grey)"/>
    <polygon points="720,540 800,470 870,540" fill="var(--yellow)"/>
    <polygon points="1120,390 1120,500 1050,450" fill="var(--yellow)"/>
  </svg>

  <h2 class="abs headline">Möglichkeiten für<br>jeden Anlass!</h2>
  <p class="abs services">Gastronomie<br>Konferenzen | Teamevents<br>Spiele | Wasserparks | Hüpfburgen<span class="cta">Wir beraten Sie gerne!</span></p>
</section>

</body>
</html>
```